依頼詳細
新規の取引の際にもホームページや会社案内を見て頂き、安心してお取引いただけるようになればと考えております。

日々お客様からご依頼いただき、買い取らせていただいている様々な金属を具体的にホームページに掲載し、こんなものも買い取ってもらえるんだということをお客様に知っていただければと考えております。

個人から個人事業主、法人のお客様の開拓と、栃木県内だけでなくより広範囲のお客様の開拓も行っていきます。

画像等は、有料素材サイトなどからのご提案もお願いいたします。
会社のロゴは、添付のロゴ写真を参考にして下さい。(株)ではなく株式会社にして下さい。フォントは同じようなものでお願いします。
サイトURL
ページ数
1ページ
希望イメージ
シンプル 複雑
単色 カラフル
暗い 明るい
日常 高級
遊び心 厳粛
未来的 伝統的
女性的 男性的
希望する色
青系、ロゴの色をメインカラーにして下さい。
納品ファイル
• 高解像度JPG (.jpg)
• イラストレーター形式 (.ai)
• フォトショップ形式 (.psd)
補足説明
レスポンシブデザインにてご提案をお願い致します。
スマートフォンのデザインもご提示いただければと思います。
お世話になっております。もう提案をいただきたいと思います。
よろしくお願いいたします。
■ 選んだ理由

お客様が大変悩まれておりましたが、素晴らしいデザインといっていただけました。ありがとうございました。今後修正等があるかと思いますが引き続きよろしくお願いします。

■ 提案者全員のお礼・コメント

たくさんのデザインありがとうございました。
お客様も大変悩まれておりました。
今後もデザインコンペを行ってまいりますのでよろしくお願いいたします。

```html
<!DOCTYPE html>
<html lang="ja">
<head>
<meta charset="utf-8">
<title>株式会社 青葉金属 | 金属・非鉄金属買取</title>
<link href="https://fonts.googleapis.com/css2?family=Noto+Sans+JP:wght@400;500;700;900&display=swap" rel="stylesheet">
<style>
:root{
  --blue:#3c4aa6;
  --navy:#1f2a6b;
  --red:#c8333a;
  --ink:#333844;
  --muted:#7a7f8c;
  --line:#dfe2ea;
  --pale:#f2f3f7;
  --white:#ffffff;
  --steel1:#c9ccd2;
  --steel2:#8e939c;
}
*{margin:0;padding:0;box-sizing:border-box}
html,body{width:1200px;height:2868px;overflow:hidden}
body{font-family:"Noto Sans JP",sans-serif;color:var(--ink);background:var(--white);font-size:13px;line-height:1.8;position:relative}
.site-header{height:60px;display:flex;align-items:center;justify-content:space-between;padding:0 40px}
.brand{font-size:22px;font-weight:700;color:var(--navy)}
.contact{text-align:right;font-size:10px;color:var(--muted);line-height:1.3}
.contact .tel{display:flex;align-items:center;gap:6px;font-size:24px;font-weight:700;color:var(--red)}
.global-nav{height:28px;background:var(--pale);border-top:1px solid var(--line);border-bottom:1px solid var(--line);display:flex;justify-content:center}
.global-nav a{width:150px;text-align:center;font-size:11px;line-height:28px;color:var(--ink);text-decoration:none;border-left:1px solid var(--line)}
.global-nav a:last-child{border-right:1px solid var(--line)}
.hero{height:292px;background:linear-gradient(180deg,#e6e8ec,#b9bdc4 60%,#9da2ab);text-align:center;position:relative;overflow:hidden}
.hero h1{padding-top:28px;font-size:40px;font-weight:900;color:var(--navy);letter-spacing:3px;line-height:1.3}
.hero p{font-size:20px;font-weight:700;color:var(--navy);letter-spacing:2px}
.hero-photos{position:absolute;left:0;right:0;bottom:20px;display:flex;justify-content:center;gap:14px}
.hero-photos div{width:150px;height:130px;border-radius:50%;background:radial-gradient(circle at 40% 35%,#f0f1f3,var(--steel2) 70%,#5d626b)}
.commit{height:280px;background:var(--blue);color:var(--white);text-align:center;padding-top:36px}
.commit h2{font-size:20px;font-weight:700;margin-bottom:22px}
.commit p{width:720px;margin:0 auto;font-size:12px;line-height:2;text-align:left;opacity:.9}
.about{background:var(--pale);height:360px;text-align:center;padding-top:48px}
.sec-title{font-size:22px;font-weight:700;color:var(--navy);margin-bottom:24px}
.about p{width:720px;margin:0 auto 30px;text-align:left;font-size:12px;line-height:2}
.btn{display:inline-block;padding:6px 26px;background:var(--blue);color:var(--white);font-size:11px;text-decoration:none}
.results{width:736px;margin:30px auto 0;display:grid;grid-template-columns:repeat(5,1fr);grid-auto-rows:164px;gap:4px}
.results .ph{background:linear-gradient(135deg,var(--steel1),var(--steel2))}
.results .ph:nth-child(3n){background:linear-gradient(135deg,#c89a6a,#7b5a3c)}
.results .ph:nth-child(4n){background:linear-gradient(135deg,#9aa0aa,#4b5059)}
.results .label{background:var(--navy);color:var(--white);font-size:20px;font-weight:700;display:flex;align-items:flex-start;padding:16px}
.results .wide{grid-column:span 2}
.results .more{background:var(--navy);display:flex;align-items:center;justify-content:center}
.results .more span{border:1px solid var(--white);color:var(--white);font-size:11px;padding:4px 22px}
.faq{text-align:center;padding-top:40px}
.faq-list{width:800px;margin:0 auto;display:flex;gap:12px}
.faq-card{flex:1;border:1px solid var(--line);text-align:left;background:var(--white)}
.faq-card h3{background:var(--navy);color:var(--white);font-size:12px;font-weight:500;padding:6px 12px}
.faq-card ul{list-style:none;padding:10px 12px}
.faq-card li{font-size:10px;line-height:1.6;padding:6px 0 6px 20px;position:relative;border-bottom:1px dotted var(--line)}
.faq-card li::before{content:"Q";position:absolute;left:0;top:7px;width:14px;height:14px;border-radius:50%;background:var(--red);color:var(--white);font-size:9px;line-height:14px;text-align:center}
.faq-card .more-link{display:block;margin:0 12px 12px;border:1px solid var(--line);text-align:center;font-size:10px;color:var(--muted)}
.items{text-align:center;padding-top:50px}
.item-list{width:800px;margin:0 auto;display:flex;gap:16px}
.item{flex:1;text-align:left}
.item .ph{height:160px}
.item h3{font-size:12px;font-weight:700;margin:8px 0 4px;color:var(--navy)}
.item p{font-size:10px;line-height:1.7;color:var(--muted)}
.news{text-align:center;padding-top:50px}
.news ul{width:800px;margin:0 auto;list-style:none}
.news li{display:flex;gap:20px;text-align:left;font-size:11px;padding:10px 16px;border-bottom:1px solid var(--line)}
.news li:nth-child(odd){background:var(--pale)}
.news time{color:var(--muted);width:90px}
.news .tag{background:var(--blue);color:var(--white);font-size:10px;padding:0 10px}
.site-footer{position:absolute;left:0;right:0;top:2650px;text-align:center}
.foot-nav{display:flex;justify-content:center;gap:28px;font-size:11px;margin-bottom:28px}
.foot-nav a{color:var(--ink);text-decoration:none}
.site-footer .brand{margin-bottom:20px}
.copy{font-size:10px;color:var(--muted)}
</style>
</head>
<body>
<header class="site-header">
  <div class="brand">株式会社 青葉金属</div>
  <div class="contact">お気軽にお問い合わせください
    <div class="tel"><svg width="20" height="20" viewBox="0 0 24 24"><path fill="#c8333a" d="M6.6 10.8a15 15 0 0 0 6.6 6.6l2.2-2.2a1 1 0 0 1 1-.25 11.4 11.4 0 0 0 3.6.57 1 1 0 0 1 1 1V20a1 1 0 0 1-1 1A17 17 0 0 1 3 4a1 1 0 0 1 1-1h3.5a1 1 0 0 1 1 1c0 1.250.2 2.45.57 3.57a1 1 0 0 1-.25 1z"/></svg>0282-00-4815</div>
  </div>
</header>
<nav class="global-nav"><a>会社概要</a><a>買取について</a><a>買取の流れ</a><a>買取実績</a><a>よくある質問</a><a>お問い合わせ</a></nav>

<section class="hero">
  <h1>迅速対応、完璧な仕事</h1>
  <p>金属・非鉄金属買取致します</p>
  <div class="hero-photos" role="img" aria-label="買取した金属部品や素材の写真">
    <div></div><div></div><div></div><div></div><div></div><div></div>
  </div>
</section>

<section class="commit">
  <h2>青葉金属のこだわり</h2>
  <p>私たちは鉄スクラップ、アルミ、ステンレス、銅、真鍮など様々な金属を一つ一つ丁寧に査定し、適正な価格で買取いたします。個人のお客様から法人のお客様まで、少量から大量まで迅速に対応いたします。県内だけでなく広い地域からのご依頼にもお応えし、安心してお取引いただける体制を整えております。長年の経験と信頼をもとに、お客様に満足いただける仕事をお約束いたします。まずはお気軽にご相談ください。</p>
</section>

<section class="about">
  <h2 class="sec-title">買取について</h2>
  <p>当社では鉄、アルミ、ステンレス、銅、真鍮、電線、モーターなど様々な金属を買取しております。こんなものも買い取ってもらえるのかと思われる品でも、まずはお問い合わせください。専門のスタッフが状態や量を確認し、その日の相場に合わせた適正な価格をご提示いたします。お持ち込みはもちろん、出張での引き取りにも対応しておりますので、ご都合に合わせてお選びいただけます。</p>
  <a class="btn">買取の流れ</a>
</section>

<section class="results" aria-label="買取実績">
  <div class="label">買取実績</div>
  <div class="ph" role="img" aria-label="ボルトやナットの写真"></div>
  <div class="ph" role="img" aria-label="銅線の写真"></div>
  <div class="ph" role="img" aria-label="金属部品の写真"></div>
  <div class="ph" role="img" aria-label="真鍮部品の写真"></div>
  <div class="ph wide" role="img" aria-label="エンジン部品の写真"></div>
  <div class="ph" role="img" aria-label="ステンレス部品の写真"></div>
  <div class="ph" role="img" aria-label="ねじ棒の写真"></div>
  <div class="ph" role="img" aria-label="銅くずの写真"></div>
  <div class="ph" role="img" aria-label="ベアリングの写真"></div>
  <div class="ph" role="img" aria-label="金属スクラップの写真"></div>
  <div class="ph" role="img" aria-label="アルミ部品の写真"></div>
  <div class="ph" role="img" aria-label="歯車の写真"></div>
  <div class="more"><span>MORE</span></div>
</section>

<section class="faq">
  <h2 class="sec-title" style="margin-top:10px">よくある質問</h2>
  <div class="faq-list">
    <div class="faq-card"><h3>カテゴリー1について</h3><ul><li>どんな金属を買い取っていますか？</li><li>少量でも買取できますか？</li><li>査定に費用はかかりますか？</li></ul><span class="more-link">もっと見る</span></div>
    <div class="faq-card"><h3>カテゴリー2について</h3><ul><li>出張引き取りはできますか？</li><li>対応エリアはどこですか？</li><li>予約は必要ですか？</li></ul><span class="more-link">もっと見る</span></div>
    <div class="faq-card"><h3>カテゴリー3について</h3><ul><li>支払い方法を教えてください。</li><li>法人取引は可能ですか？</li><li>領収書は出ますか？</li></ul><span class="more-link">もっと見る</span></div>
    <div class="faq-card"><h3>カテゴリー4について</h3><ul><li>必要な書類はありますか？</li><li>営業時間を教えてください。</li><li>相場はどう決まりますか？</li></ul><span class="more-link">もっと見る</span></div>
  </div>
</section>

<section class="items">
  <h2 class="sec-title">買い取れるもの</h2>
  <div class="item-list">
    <div class="item"><div class="ph" role="img" aria-label="ステンレスパイプの写真" style="background:linear-gradient(135deg,#e4e6ea,#8e939c)"></div><h3>買取可能金属名</h3><p>鉄、アルミ、ステンレスなどの説明文がここに入ります。</p></div>
    <div class="item"><div class="ph" role="img" aria-label="銅線の巻きの写真" style="background:linear-gradient(135deg,#e0a878,#8a5530)"></div><h3>買取可能金属名</h3><p>銅線や電線などの説明文がここに入ります。</p></div>
    <div class="item"><div class="ph" role="img" aria-label="金属棒の写真" style="background:linear-gradient(135deg,#d2d5da,#5d626b)"></div><h3>買取可能金属名</h3><p>金属棒や板材などの説明文がここに入ります。</p></div>
    <div class="item"><div class="ph" role="img" aria-label="銅パイプの写真" style="background:linear-gradient(135deg,#e8b080,#9a5a2e)"></div><h3>買取可能金属名</h3><p>銅パイプや真鍮などの説明文がここに入ります。</p></div>
  </div>
</section>

<section class="news">
  <h2 class="sec-title">新着情報</h2>
  <ul>
    <li><time>2017.00.00</time><span class="tag">お知らせ</span>ホームページをリニューアルいたしました。</li>
    <li><time>2017.00.00</time><span class="tag">お知らせ</span>年末年始の営業日についてのご案内です。</li>
    <li><time>2017.00.00</time><span class="tag">お知らせ</span>買取実績を更新いたしました。</li>
    <li><time>2017.00.00</time><span class="tag">お知らせ</span>出張引き取りの対応エリアを拡大しました。</li>
    <li><time>2017.00.00</time><span class="tag">お知らせ</span>夏季休業のお知らせです。</li>
  </ul>
</section>

<footer class="site-footer">
  <nav class="foot-nav"><a>会社概要</a><a>買取について</a><a>買取の流れ</a><a>買取実績</a><a>よくある質問</a><a>お問い合わせ</a></nav>
  <div class="brand">株式会社 青葉金属</div>
  <p class="copy">Copyright © 株式会社 青葉金属 All Rights Reserved.</p>
</footer>
</body>
</html>
```